Seven nights at the harbour

Creation of the cover for the book: "Sept nuits sur le quai du port" with the joined photo of a 70 years old lady.
Title: "Seven nights along the old harbour"
Author: "Mireille Vaston"
Publisher: "Editions Morvane" (should be at the bottom of the page)
Format: 14 x 20.5 cm
The story: A senior lady (70 years old), divorced, with a beautiful face, still wants to seduce, even young men.
We found the perfect photo for the woman. We would like to ask you to make a modern cover from it.
Besoin de quelques jours pour choisir un design
Target Market(s)
Novels reader (adults)
Industry/Entity Type
book

```html
<!DOCTYPE html>
<html lang="en">
<head>
<meta charset="utf-8">
<title>Seven Nights along the Old Harbour — Cover</title>
<link href="https://fonts.googleapis.com/css2?family=Roboto+Condensed:wght@300;700&family=Roboto:wght@400&display=swap" rel="stylesheet">
<style>
  :root {
    --page-bg: #ececec;
    --ink-black: #0b0b0b;
    --band-red: #dc1a24;
    --band-red-dark: #a5111a;
    --paper-white: #f6f6f4;
    --paper-shade: #d9d9d6;
    --hair-bright: #e4e7e8;
    --hair-light: #c9cdcf;
    --hair-mid: #9ea4a6;
    --hair-dark: #5f6668;
    --skin: #c99684;
    --publisher-red: #e0232b;
  }
  * { margin: 0; padding: 0; box-sizing: border-box; }
  html, body {
    width: 908px;
    height: 1200px;
    overflow: hidden;
    background: var(--page-bg);
  }
  .cover {
    position: absolute;
    left: 114px;
    top: 40px;
    width: 680px;
    height: 1120px;
    background: var(--ink-black);
    overflow: hidden;
    box-shadow: 0 6px 24px rgba(0,0,0,0.18);
  }
  .cover-photo {
    position: absolute;
    left: 0;
    top: 0;
    width: 680px;
    height: 780px;
    background:
      radial-gradient(ellipse 14% 18% at 50% 38%, rgba(201,150,132,0.85), rgba(201,150,132,0) 80%),
      radial-gradient(ellipse 16% 10% at 45% 6%, rgba(201,150,132,0.5), rgba(201,150,132,0) 80%),
      radial-gradient(ellipse 30% 22% at 22% 30%, var(--hair-bright), rgba(228,231,232,0) 75%),
      radial-gradient(ellipse 28% 26% at 78% 55%, var(--hair-bright), rgba(228,231,232,0) 75%),
      radial-gradient(ellipse 12% 16% at 56% 62%, rgba(60,64,66,0.55), rgba(60,64,66,0) 80%),
      linear-gradient(160deg, var(--hair-mid) 0%, var(--hair-light) 30%, var(--hair-mid) 55%, var(--hair-light) 75%, var(--hair-dark) 100%);
  }
  .cover-shapes {
    position: absolute;
    left: 0;
    top: 0;
    width: 680px;
    height: 1120px;
  }
  .title {
    position: absolute;
    left: 70px;
    top: 690px;
    font-family: "Roboto Condensed", "Arial Narrow", sans-serif;
    font-size: 66px;
    line-height: 100px;
    color: var(--paper-white);
    letter-spacing: -0.5px;
    white-space: nowrap;
    text-shadow: 2px 3px 4px rgba(0,0,0,0.4);
    transform: rotate(1deg);
    transform-origin: left top;
  }
  .title .strong { font-weight: 700; }
  .title .light { font-weight: 300; }
  .author {
    position: absolute;
    left: 78px;
    top: 952px;
    font-family: "Roboto", Arial, sans-serif;
    font-size: 35px;
    font-weight: 400;
    color: var(--paper-white);
    text-transform: uppercase;
  }
  .publisher {
    position: absolute;
    left: 78px;
    top: 1018px;
    font-family: "Roboto", Arial, sans-serif;
    font-size: 22px;
    font-weight: 400;
    color: var(--publisher-red);
  }
</style>
</head>
<body>
  <main class="cover">
    <div class="cover-photo" role="img" aria-label="Portrait photograph of a seventy-year-old woman with long windswept silver hair covering most of her face"></div>

    <svg class="cover-shapes" viewBox="0 0 680 1120" aria-hidden="true">
      <defs>
        <linearGradient id="band-red-fill" x1="0" y1="0" x2="1" y2="1">
          <stop offset="0" stop-color="var(--band-red)"/>
          <stop offset="1" stop-color="var(--band-red-dark)"/>
        </linearGradient>
        <linearGradient id="curl-fill" x1="0" y1="0" x2="1" y2="0">
          <stop offset="0" stop-color="var(--paper-white)"/>
          <stop offset="0.7" stop-color="#ededeb"/>
          <stop offset="1" stop-color="var(--paper-shade)"/>
        </linearGradient>
      </defs>

      <polygon class="torn-paper" fill="var(--paper-white)"
        points="0,655 8,648 14,652 22,641 30,650 37,646 45,655 52,644 58,649 66,638 75,647 83,643 92,652 99,640 108,646 118,636 126,645 135,641 144,651 152,643 161,647 170,635 178,644 188,640 197,650 206,642 214,648 224,637 233,646 243,641 252,652 262,645 271,650 281,642 290,653 300,648 310,657 320,650 330,661 340,655 350,666 361,660 371,671 380,664 391,676 401,670 412,682 422,676 433,688 443,682 454,694 464,689 475,701 486,695 497,707 508,702 519,714 530,709 541,721 552,716 563,727 574,722 586,735 597,730 608,742 620,737 632,746 680,752
        680,1000 630,990 614,994 600,977 587,988 574,970 560,981 547,964 534,975 521,958 508,968 494,952 481,963 468,946 455,956 441,940 428,951 415,933 402,944 388,928 375,939 362,921 349,932 335,916 322,927 309,909 296,920 283,904 270,914 256,898 244,909 231,892 218,902 206,886 193,897 180,880 168,890 156,874 143,884 131,868 118,880 106,862 95,872 82,858 70,868 60,852 47,864 38,848 27,856 16,838 9,850 0,842"/>

      <polygon class="title-band" fill="url(#band-red-fill)"
        points="0,672 10,666 19,674 28,663 40,671 51,667 60,676 72,662 84,672 96,668 105,677 118,660 130,670 142,666 154,675 166,658 178,669 190,664 203,673 215,661 228,670 240,666 252,676 265,664 277,672 290,668 303,679 316,672 329,684 342,678 355,690 368,682 381,695 394,688 407,700 420,694 433,707 446,700 459,713 472,706 485,720 498,713 511,727 524,720 537,733 550,727 563,740 576,734 589,748 602,741 615,754 640,760 680,768
        680,990 640,985 620,980 606,968 592,976 578,960 564,969 550,954 536,962 521,946 508,954 493,938 479,946 466,930 452,938 437,922 424,931 410,915 396,924 382,908 368,916 353,900 340,909 326,893 312,901 298,886 284,894 270,878 256,886 242,871 228,879 214,864 200,871 186,857 172,864 158,849 145,857 131,842 117,849 103,835 90,842 76,828 63,835 49,822 37,828 24,815 12,822 0,812"/>

      <path class="page-curl" fill="url(#curl-fill)"
        d="M630,752 L680,742 L680,1120 L674,1120 Q640,960 630,752 Z"/>
    </svg>

    <h1 class="title">
      <span class="strong">Seven Nights</span> <span class="light">along</span><br>
      <span class="light">the</span> <span class="strong">Old Harbour</span>
    </h1>

    <p class="author">Mireille Vaston</p>
    <p class="publisher">Publisher: Editions Morvane</p>
  </main>
</body>
</html>
```